Harbor Chapel San Francisco needs a Servant Handbook designed.

We need a Servant Handbook to be designed and formatted. The content is currently 27 pages and involves headings, quotes, bolded statements and scripture that we would like to stick out. We also need a cover designed for it as well. Cover - "Harbor Leadership Development"

Here is a link to our Harbor Chapel style guide.
https://studio-31862.brandvault.example/d/7QpWnRkLz2Vb/harbor-chapel-style-guide

Target Market(s)

Leaders within our church.

Font styles to use
Sans Serif

```html
<!DOCTYPE html>
<html lang="en">
<head>
<meta charset="utf-8">
<title>Harbor Chapel Servant Handbook – Pages 7–9</title>
<link href="https://fonts.googleapis.com/css2?family=Lato:ital,wght@0,400;0,700;1,400&display=swap" rel="stylesheet">
<style>
  :root {
    --backdrop: #e8e9ea;
    --paper: #ffffff;
    --ink: #2e2e2e;
    --ink-strong: #1a1a1a;
    --green: #6cbf3f;
    --green-soft: rgba(108, 191, 63, 0.16);
    --link: #5aa832;
  }
  * { box-sizing: border-box; margin: 0; padding: 0; }
  html, body { width: 844px; height: 1200px; overflow: hidden; }
  body {
    position: relative;
    background: var(--backdrop);
    font-family: "Lato", "Helvetica Neue", Arial, sans-serif;
    color: var(--ink);
  }
  .divider {
    position: absolute; left: 0; top: 594px; width: 844px; height: 4px;
    background: #ffffff;
  }
  .page-label {
    position: absolute; width: 120px; text-align: center;
    font-size: 13px; color: #222; letter-spacing: 0.2px;
  }
  .page {
    position: absolute; width: 356px; height: 504px;
    background: var(--paper);
    box-shadow: 2px 3px 5px rgba(0,0,0,0.28);
    overflow: hidden;
  }
  .page-body {
    position: absolute; left: 41px; top: 34px; width: 274px;
    font-size: 6.3px; line-height: 1.3;
    text-align: justify;
  }
  .page-body p, .page-body ul, .callout, .subhead { margin-bottom: 7.5px; }
  .page-body ul { list-style: none; }
  .page-body li { position: relative; padding-left: 8px; margin-bottom: 6px; }
  .page-body li::before {
    content: ""; position: absolute; left: 0; top: 1.6px;
    width: 4px; height: 4px; border-radius: 50%; background: var(--ink-strong);
  }
  .page-body ul.tight li { margin-bottom: 0; }
  .callout {
    font-weight: 700; color: var(--ink-strong);
    background: linear-gradient(90deg, var(--green-soft) 0%, rgba(108,191,63,0.08) 55%, rgba(108,191,63,0) 100%);
    padding: 2px 0 2px 0; margin-left: -2px; padding-left: 2px;
  }
  .subhead { margin-bottom: 0; }
  .subhead + p, .subhead + ul { margin-top: 1px; }
  .callout.subhead { padding: 1px 2px; }
  .page-body a { color: var(--link); font-weight: 700; text-decoration: none; }
  .footer-stripes {
    position: absolute; left: 0; top: 469px; width: 315px;
  }
  .footer-stripes span {
    display: block; height: 3px; background: var(--green); margin-bottom: 5px;
  }
</style>
</head>
<body>
  <div class="divider"></div>

  <div class="page-label" style="left:177px; top:15px;">Pg-7</div>
  <div class="page-label" style="left:535px; top:15px;">Pg-8</div>
  <div class="page-label" style="left:177px; top:621px;">Pg-9</div>

  <!-- Page 7 -->
  <section class="page" style="left:54px; top:42px;">
    <div class="page-body">
      <p>In his book, The Rested Leader, Daniel Okafor gives some questions that can help us see what we need to be doing with our time:</p>
      <ul>
        <li>What do you currently do that nurtures your spirit and fills you with delight?</li>
        <li>What people, places, and activities do you need to avoid because they deplete you or make it difficult for you to remain anchored in Christ?</li>
        <li>What “have to’s” impact your rhythms in this season of life? (These could be caring for aging parents, raising a young child, dealing with health issues, etc.)</li>
      </ul>
      <p class="callout">Practicing a weekly Sabbath time is critical for leaders.</p>
      <p>Some of you may think you or your role is too important to practice the Sabbath. Just think about that for a moment. So God weaves this principle into the universe, He observes it, He rests from His work...but you and your work are too important? Because you lead a massive company? Because you’re working on the next game? Because we want Harbor to be the most amazing church ever? Who do we think we are?</p>
      <p class="callout">Sabbath-keeping is the primary discipline that helps us to live within the limits of our humanity and to honor God as our Creator. (Miriam Hale Corwin)</p>
      <p>“Emotionally unhealthy leaders do not practice Sabbath - a weekly, twenty-four-hour period in which they cease all work and rest, delight in God’s gifts, and enjoy life with him.” - Daniel Okafor, <em>The Rested Leader</em></p>
      <p>Practical Thoughts for Observing Sabbath:</p>
      <ul>
        <li>24 hours might seem impossible. But choose some block of time each week...preferably the same time, same day each week - to establish a rhythm.<br>Unplug from technology during this time.<br>Worship. Pray. Delight in God’s creation. Take a walk. Listen to music. Enjoy. Take a nap.</li>
        <li>The practice of Sabbath will remind you that God is holding your world up.</li>
        <li>You will re-enter your work with renewed energy, renewed thinking, and a renewed heart.</li>
      </ul>
      <p class="callout">The Importance of Self-Leadership</p>
      <p>We can all agree that leading others can be quite the challenge. Sometimes people aren’t as nice as we wish they were. Sometimes people aren’t as competent as we would prefer them to be. Sometimes people are critical of our leadership. Leading people can be a real challenge. Who would you say is the most difficult person for you to lead?</p>
      <p>The most difficult person you will ever lead is YOU.</p>
    </div>
    <div class="footer-stripes"><span></span><span></span><span></span></div>
  </section>

  <!-- Page 8 -->
  <section class="page" style="left:434px; top:42px;">
    <div class="page-body">
      <p class="callout">“Before we can conquer the world, we must first conquer the self.” - R. Albright Morrow, <em>Leading from Within</em></p>
      <p>“Throughout the Bible we find a pattern where God impacts a key leader before He uses that leader to accomplish greater things with the group he/she leads.” - Glen Whitcomb, Kinship Church</p>
      <p class="callout">“Nothing so conclusively proves a man’s ability to lead others as what he does from day to day to lead himself.” – Howard Pell, former chairman of Norvane Systems</p>
      <p>Not only is self-leadership really important; so is self-awareness. Self-awareness doesn’t mean self-interest or self-absorption. So many people today seem to be obsessed about themselves. This is not what we are talking about. Self-awareness is being aware of how God has uniquely made you as a person and called you as a leader. How can you discover your purpose in life?</p>
      <p class="callout">“The search for the purpose of life has puzzled people for thousands of years. That’s because we typically begin at the wrong starting point – ourselves...You didn’t create yourself, so there is no way you can tell yourself what you were created for.” Calvin Brandt, <em>A Life Well Aimed</em></p>
      <p>What specific gifts and abilities has God given to you? This might be a good time to talk about the difference between our natural abilities and our supernatural abilities, or what we refer to as our “spiritual gifts”. God has given every person on planet earth natural gifts and abilities.</p>
      <p class="callout subhead">Natural Abilities</p>
      <ul class="tight">
        <li>What you do well</li>
        <li>What tends to come easier to you than to the rest of us</li>
        <li>Don’t have to be a Christian to have natural abilities (obviously)</li>
        <li>You can discern some of these abilities or strengths through assessments like Strengths Mapper (http://www.strengthsmapper.example/)</li>
      </ul>
      <p style="margin-top:7.5px;">Glen Whitcomb, a pastor in Oregon, created a framework that can help you think about your abilities and gifting. Spend some time thinking about things you do in life that fall into the following categories: what you’re bad at, what you’re good at, what you’re excellent at, and what are your unique abilities.</p>
      <p class="callout subhead">Things You’re Bad At</p>
      <p>This is something that you do poorly—you might even be incompetent at it—but you have to do it to make it through your day. In the early days of a company or a church or almost anything – you have to do things that you may not be suited for at all.</p>
    </div>
    <div class="footer-stripes"><span></span><span></span><span></span></div>
  </section>

  <!-- Page 9 -->
  <section class="page" style="left:54px; top:647px;">
    <div class="page-body" style="top:35px;">
      <p class="callout subhead">Things You’re Good At</p>
      <p>This is an area where you have sufficient skill, but no one would pay you to do it fulltime. Maybe you’re an amazing travel agent. You know how to discover the tricks that bring the best deals on travel, but no one is going to pay you to do that as your main job.</p>
      <p class="callout subhead">Things You’re Excellent At</p>
      <p>You excel in this area and are highly competent, and if you had to, you could do it professionally.</p>
      <p class="callout subhead">Your Unique Ability</p>
      <p>This is what God knit you in your mother’s womb to do. Not only do you excel at this, but you feel most alive when doing it.</p>
      <p>This seems like a simple assessment. However, the beauty in this exercise is in figuring out the difference between the things you excel at and what your unique abilities are. To the outside world, these two look identical. You have success in both. People seek you out to hear your wisdom on both. The difference then? One of these will drain you, while the other one will energize you.</p>
      <p>The goal is to try to spend as much of our time and energy working in these “unique abilities”.</p>
      <p class="callout">*Disclaimer: Sometimes God calls us to do things outside of our giftings. Do WHATEVER God calls you to do. But we need to know that the general rule about our natural gifts is that God gives them to us so that we employ our gifts and use the abilities He gave to us.</p>
      <p class="callout">Spiritual Gifts</p>
      <p>“Spiritual leadership requires superior spiritual power, which can never be generated by the self. There is no such thing as a self-made spiritual leader.” – R. Albright Morrow, <em>Leading from Within</em></p>
      <p style="text-align:left;">“Spiritual gifts are special abilities given by the Holy Spirit and distributed to every<br>believer according to God’s design and grace for the common good of the body of<br>Christ.” –Alan Pryor and Neil Dawes, <em>Connected</em></p>
      <p>If it’s been a while since you have taken a Spiritual Gifts test, let me encourage you to do that now. You can take a test for free at <a>https://www.giftsprofile.example/</a> You will receive a report. We want to encourage you to email this report to your Harbor coach or to an Harbor staff member. Plan a time to discuss your results with them.</p>
      <p class="callout">It’s not enough to recognize the spiritual gifts God has given to us. We must also find ways to employ those gifts. Based on your gifts, what areas should you be serving – in the church, in the community, in your job, or in any other arenas?</p>
      <p class="callout">Harbor Leaders are Servants.</p>
    </div>
    <div class="footer-stripes"><span></span><span></span><span></span></div>
  </section>
</body>
</html>
```